"Cork Hollow Excursions" is a top notch Santa Barbara County Wine Tour company.

We provide scenic, boutique and custom wine tours. I need the card to be clean and classy. I will provide our logo. I would like the logo to cover the back side of the card as an option and would like to see a couple color options other then our signature green and gold. I would like to see some creative options and let the designers come up with options.
I need cards for myself and my team. The final design should communicate "An authentic and boutique wine tour experience"
Please use my website for reference www.corkhollowexcursions.com

Target Market(s)

We have a wide range of clients from millennials to baby boomers

Industry/Entity Type

Tour

Contact Information for Business Card

Contact info:
Dale Munford
805-291-6384
info@corkhollowexcursions.com
corkhollowexcursions.com

Colors

Designer to choose colors to be used in the design.

Requirements
Must have
• my logo
Nice to have
• *I would like to have the backside side with the logo and the company statement
• "An authentic and boutique wine tour experience" as an option.
• *I would also like to see what the designers can create!
• *I would like to see an option that incorporates or social: snapgrid, rovia, route scout
Should not have
• I do not want it too busy.

```html
<!DOCTYPE html>
<html lang="en">
<head>
<meta charset="utf-8">
<title>Cork Hollow Excursions – Business Card</title>
<link rel="stylesheet" href="https://fonts.googleapis.com/css2?family=Cinzel:wght@400;500&family=Lora:ital,wght@0,400;1,400&display=swap">
<style>
  :root {
    --green: #1f7a4a;
    --green-deep: #17603a;
    --green-light: #2e9160;
    --gold: #b08d6a;
    --gold-light: #d8c2a8;
    --paper: #f7f7f5;
    --backdrop: #ece9e3;
    --ink: #3a3a3a;
  }
  * { margin: 0; padding: 0; box-sizing: border-box; }
  html, body { width: 1200px; height: 780px; overflow: hidden; }
  body {
    background: var(--backdrop);
    display: flex;
    align-items: center;
    justify-content: center;
    gap: 40px;
    font-family: "Lora", Georgia, serif;
  }
  .card {
    position: relative;
    width: 540px;
    height: 309px;
    overflow: hidden;
    box-shadow: 0 6px 18px rgba(0,0,0,.18);
  }

  /* Front */
  .card-front { background: var(--paper); }
  .front-wave { position: absolute; inset: 0; width: 100%; height: 100%; }
  .front-brand {
    position: absolute;
    top: 28px; right: 40px;
    text-align: center;
  }
  .brand-name {
    font-family: "Cinzel", Georgia, serif;
    font-weight: 400;
    font-size: 21px;
    letter-spacing: 2px;
    color: var(--gold);
    line-height: 1.1;
  }
  .brand-region {
    font-family: "Cinzel", Georgia, serif;
    font-size: 8px;
    letter-spacing: 4px;
    color: var(--green);
    margin-top: 8px;
    padding-top: 6px;
    border-top: 1px solid var(--gold-light);
    text-transform: uppercase;
  }
  .person-name {
    position: absolute;
    left: 34px; top: 138px;
    font-family: "Cinzel", Georgia, serif;
    font-weight: 400;
    font-size: 19px;
    letter-spacing: 1.5px;
    color: var(--gold);
    text-transform: uppercase;
  }
  .contact-list {
    position: absolute;
    left: 34px; top: 196px;
    list-style: none;
    font-size: 12.5px;
    color: var(--ink);
  }
  .contact-item { display: flex; align-items: center; gap: 9px; margin-bottom: 7px; }
  .contact-icon { width: 17px; height: 17px; flex: none; }

  /* Back */
  .card-back {
    background: radial-gradient(ellipse at 55% 45%, var(--green-light) 0%, var(--green) 55%, var(--green-deep) 100%);
    color: #fff;
    display: flex;
    flex-direction: column;
    align-items: center;
    justify-content: center;
  }
  .back-brand { text-align: center; }
  .back-brand .brand-name { color: #fff; font-size: 25px; }
  .back-brand .brand-region {
    color: #fff;
    border-top-color: rgba(255,255,255,.55);
    font-size: 9px;
  }
  .social-list {
    list-style: none;
    display: flex;
    gap: 20px;
    margin-top: 22px;
    font-size: 10.5px;
    letter-spacing: .5px;
  }
  .social-item { display: flex; align-items: center; gap: 6px; }
  .social-dot {
    width: 14px; height: 14px; border-radius: 50%;
    border: 1.5px solid #fff;
  }
  .tagline {
    position: absolute;
    bottom: 28px;
    width: 100%;
    text-align: center;
    font-style: italic;
    font-size: 13px;
    letter-spacing: 1.5px;
    color: rgba(255,255,255,.9);
  }
</style>
</head>
<body>

  <section class="card card-front" aria-label="Business card front">
    <svg class="front-wave" viewBox="0 0 540 309" preserveAspectRatio="none" aria-hidden="true">
      <path d="M540 132 C485 138 455 172 435 218 C410 276 340 298 240 309 L540 309 Z" fill="var(--green)"/>
      <path d="M530 134 C478 142 449 176 428 222 C402 278 336 298 228 309" fill="none" stroke="var(--gold)" stroke-width="2.5"/>
    </svg>

    <div class="front-brand">
      <div class="brand-name">Cork Hollow<br>Excursions</div>
      <div class="brand-region">Santa Barbara County</div>
    </div>

    <h1 class="person-name">Dale Munford</h1>

    <ul class="contact-list">
      <li class="contact-item">
        <svg class="contact-icon" viewBox="0 0 20 20" aria-hidden="true"><circle cx="10" cy="10" r="9" fill="none" stroke="var(--green)" stroke-width="1.6"/><path d="M7 5.5l2 2-1 1.3c.6 1.3 1.6 2.3 2.9 2.9l1.3-1 2 2-1.3 1.6c-3.6-.4-6.9-3.7-7.3-7.3z" fill="var(--green)"/></svg>
        805-291-6384
      </li>
      <li class="contact-item">
        <svg class="contact-icon" viewBox="0 0 20 20" aria-hidden="true"><circle cx="10" cy="10" r="9" fill="none" stroke="var(--green)" stroke-width="1.6"/><rect x="5" y="6.5" width="10" height="7" fill="var(--green)"/><path d="M5 6.5l5 4 5-4" fill="none" stroke="#fff" stroke-width="1"/></svg>
        info@corkhollowexcursions.com
      </li>
      <li class="contact-item">
        <svg class="contact-icon" viewBox="0 0 20 20" aria-hidden="true"><circle cx="10" cy="10" r="9" fill="none" stroke="var(--green)" stroke-width="1.6"/><circle cx="10" cy="10" r="5" fill="none" stroke="var(--green)" stroke-width="1.2"/><path d="M5 10h10M10 5c-2 2.8-2 7.2 0 10M10 5c2 2.8 2 7.2 0 10" fill="none" stroke="var(--green)" stroke-width="1"/></svg>
        corkhollowexcursions.com
      </li>
    </ul>
  </section>

  <section class="card card-back" aria-label="Business card back">
    <div class="back-brand">
      <div class="brand-name">Cork Hollow<br>Excursions</div>
      <div class="brand-region">Santa Barbara County</div>
    </div>
    <ul class="social-list">
      <li class="social-item"><span class="social-dot"></span>snapgrid</li>
      <li class="social-item"><span class="social-dot"></span>rovia</li>
      <li class="social-item"><span class="social-dot"></span>route scout</li>
    </ul>
    <p class="tagline">An authentic and boutique wine tour experience</p>
  </section>

</body>
</html>
```